Laptop Accessories Packing Design

We are looking for a new package design of a laptop accesories (batteries, charges, hard drives etc.). We want to refresh our brand Vireo CellWorks. At VireoCell, we create high-end laptop accessories that ensure reliability, performance, and longevity for users worldwide. Our mission is to deliver innovative and durable solutions that allow users to work, create, and grow without limits.
General Packaging Concept
Minimalist and elegant look, yet with elements that catch the eye (Vireo products will mainly be offered on auction portals such as Brindle, Kiva, Tollmart, so it would be good if the packaging attracted attention and stood out from the competitors).
Should I put a photo, sketch or product icon on the box? We'll leave that to your imagination.
We ask for a general design of the packaging. After the competition, together with the winner, we will add the rest of the information to the back and sides of the box.
In the attachments there is our Logo (you can use other colors) and sample packaging of competitors
Target Market(s)
E-commerse
Industry/Entity Type
individual end customer
Look and feel
Each slider illustrates characteristics of the customer's brand and the style your logo design should communicate.

```html
<!DOCTYPE html>
<html lang="en">
<head>
<meta charset="utf-8">
<title>Vireo CellWorks – Box Dielines</title>
<link rel="stylesheet" href="https://fonts.googleapis.com/css2?family=Michroma&family=Exo+2:wght@700&family=Roboto:wght@400;700&display=swap">
<style>
:root{
  --paper:#ffffff;
  --ink:#050505;
  --panel:#0b0b0c;
  --panel-edge:#1c1c1f;
  --gold:#a97a1c;
  --gold-bright:#f2c230;
  --gold-deep:#7a5510;
  --white:#ffffff;
  --badge-blue:#1f5fb0;
  --badge-blue-light:#4a9de0;
  --fold:#2a2a2e;
}
*{margin:0;padding:0;box-sizing:border-box}
html,body{width:781px;height:1200px;overflow:hidden;background:var(--paper)}
.canvas{position:relative;width:781px;height:1200px;font-family:"Roboto",Arial,sans-serif;color:var(--white)}
.part{position:absolute;background:var(--panel);border:1px solid var(--fold);overflow:hidden}
.lid{background:radial-gradient(ellipse 40% 70% at 35% 20%,rgba(242,180,40,.55),transparent 70%),linear-gradient(180deg,#141414,#050505)}
.wing{background:radial-gradient(circle at 50% 50%,var(--gold-bright),var(--gold) 60%,var(--gold-deep));border:none}
.back{background:radial-gradient(ellipse 30% 40% at 70% 90%,rgba(242,180,40,.45),transparent 70%),linear-gradient(135deg,#0d0d0f,#050505 60%,#17171a)}
.band{background:linear-gradient(180deg,#0a0a0a,#121214 50%,#0a0a0a)}
.front{background:radial-gradient(ellipse 35% 25% at 45% 55%,rgba(242,190,50,.45),transparent 70%),linear-gradient(90deg,#0a0a0b,#151517 40%,#060606);border-radius:26px}
.bottom{background:linear-gradient(180deg,#0a0a0b,#131315);border-radius:26px}
.tab{position:absolute;background:var(--gold)}
.side-strip{position:absolute;top:0;bottom:0;background:#070707;border-left:1px solid var(--fold);border-right:1px solid var(--fold)}
.flip{transform:rotate(180deg)}
.brand{position:absolute;font-family:"Exo 2",sans-serif;font-weight:700;color:var(--white);line-height:1;text-align:center}
.brand .sub{display:block;font-family:"Roboto",sans-serif;font-weight:400;font-size:4px;letter-spacing:2.4px;margin-top:2px;background:var(--white);color:var(--ink);padding:1px 4px}
.label{position:absolute;background:var(--gold);clip-path:polygon(6% 0,100% 0,100% 100%,0 100%);font-family:"Michroma",sans-serif;font-size:10px;color:var(--white);display:flex;align-items:center;justify-content:center;letter-spacing:.5px}
.label b{font-weight:400;color:var(--white)}
.label span{color:var(--ink)}
.headline{position:absolute;font-family:"Michroma",sans-serif;line-height:1.02}
.headline .w{display:block;color:var(--white)}
.headline .g{display:block;color:var(--gold-bright)}
.badge{position:absolute;height:8px;border-radius:2px;background:linear-gradient(180deg,var(--badge-blue-light),var(--badge-blue));font-size:5px;font-weight:700;color:#dfefff;display:flex;align-items:center;justify-content:center;letter-spacing:.2px}
.photo{position:absolute}
.laptop{background:radial-gradient(ellipse at 50% 45%,#f5d060,#b8860f 55%,#2a2110);border-radius:3px;border:2px solid #222}
.laptop-base{position:absolute;height:4px;background:linear-gradient(180deg,#c9c9c9,#5a5a5a);border-radius:0 0 4px 4px}
.stripe{position:absolute;background:var(--gold);clip-path:polygon(0 0,100% 0,88% 100%,0 100%)}
.features{position:absolute;display:flex;gap:9px}
.feature{display:flex;align-items:center;gap:3px}
.feature svg{width:10px;height:12px}
.feature p{font-size:4px;font-weight:700;line-height:1.1;text-transform:uppercase}
.feature p small{display:block;font-weight:400;font-size:3.6px}
.maker{position:absolute;font-size:4px;line-height:1.3}
.web{position:absolute;font-size:4.3px;font-weight:700}
.certs{position:absolute;display:flex;gap:6px;align-items:center}
.certs i{display:block;width:9px;height:9px;background:var(--white);border-radius:50%}
.certs i.sq{border-radius:1px}
</style>
</head>
<body>
<div class="canvas">

  <!-- Box one: laptop battery -->
  <section class="box box-battery" aria-label="Laptop battery box dieline">
    <div class="part lid" style="left:131px;top:35px;width:511px;height:80px" role="img" aria-label="Golden electric sparks over dark hexagon texture"></div>
    <div class="part wing" style="left:45px;top:97px;width:91px;height:158px" role="img" aria-label="Golden circuit board texture"></div>
    <div class="part wing" style="left:639px;top:97px;width:89px;height:158px" role="img" aria-label="Golden circuit board texture"></div>
    <div class="part back" style="left:137px;top:115px;width:503px;height:129px" role="img" aria-label="Dark panel with golden sparks">
      <div class="side-strip" style="left:0;width:69px"></div>
      <div class="side-strip" style="right:0;width:72px"></div>
      <div class="tab" style="left:24px;top:-2px;width:20px;height:37px;clip-path:polygon(0 0,100% 0,100% 100%,0 80%)"></div>
      <div class="tab" style="left:456px;top:70px;width:20px;height:59px;clip-path:polygon(0 10%,100% 0,100% 100%,0 100%)"></div>
      <div class="maker flip" style="left:188px;top:14px">MANUFACTURER:<br>KORVEL Marta Zielna<br>ul. Lipowa 12<br>62-300 Wrzesnia, Poland<br>Made in China</div>
      <div class="web flip" style="left:93px;top:18px">www.vireocell.pl</div>
      <div class="certs flip" style="left:93px;top:33px"><i class="sq"></i><i class="sq"></i><i></i><i></i></div>
    </div>
    <div class="part band" style="left:128px;top:244px;width:518px;height:67px">
      <div class="brand flip" style="left:105px;top:22px;font-size:22px">Vireo<span class="sub">CELLWORKS</span></div>
      <div class="label flip" style="left:272px;top:23px;width:176px;height:20px"><b>LAPTOP&nbsp;</b><span>BATTERY</span></div>
    </div>
    <div class="part front" style="left:142px;top:311px;width:490px;height:129px">
      <div class="brand" style="left:92px;top:16px;font-size:22px">Vireo<span class="sub">CELLWORKS</span></div>
      <div class="headline" style="left:93px;top:63px;font-size:16px"><span class="w">LAPTOP</span><span class="g">BATTERY</span></div>
      <div class="badge" style="left:90px;top:100px;width:80px">PREMIUM ACCESSORIES</div>
      <div class="photo laptop" style="left:286px;top:35px;width:102px;height:60px" role="img" aria-label="Laptop with glowing golden screen"></div>
      <div class="laptop-base" style="left:270px;top:95px;width:134px"></div>
    </div>
    <div class="part bottom" style="left:142px;top:440px;width:490px;height:82px">
      <div class="stripe" style="left:44px;top:24px;width:82px;height:20px"></div>
      <div class="features" style="left:146px;top:28px">
        <div class="feature"><svg viewBox="0 0 10 12"><path d="M5 0L10 2v4c0 3-2.5 5-5 6C2.5 11 0 9 0 6V2z" fill="#fff"/><rect x="4.4" y="2.5" width="1.2" height="5" fill="#000"/><circle cx="5" cy="8" r="1.3" fill="#000"/></svg><p>Overheat<small>Protection</small></p></div>
        <div class="feature"><svg viewBox="0 0 10 12"><path d="M5 0L10 2v4c0 3-2.5 5-5 6C2.5 11 0 9 0 6V2z" fill="#fff"/><path d="M5.5 2L3.5 6.5h2L4.5 10l2.5-5h-2z" fill="#000"/></svg><p>Overvoltage<small>Protection</small></p></div>
        <div class="feature"><svg viewBox="0 0 10 12"><path d="M5 0L10 2v4c0 3-2.5 5-5 6C2.5 11 0 9 0 6V2z" fill="#fff"/><rect x="2" y="5.5" width="6" height="1" fill="#000"/><rect x="4.5" y="3" width="1" height="6" fill="#000"/></svg><p>Overcurrent<small>Protection</small></p></div>
        <div class="feature"><svg viewBox="0 0 10 12"><path d="M5 0L10 2v4c0 3-2.5 5-5 6C2.5 11 0 9 0 6V2z" fill="#fff"/><path d="M5 3l3 5H2z" fill="#000"/></svg><p>Short-circuit<small>Protection</small></p></div>
      </div>
    </div>
  </section>

  <!-- Box two: AC adapter -->
  <section class="box box-adapter" aria-label="AC adapter box dieline">
    <div class="part lid" style="left:185px;top:587px;width:403px;height:73px" role="img" aria-label="Golden electric sparks over dark hexagon texture"></div>
    <div class="part wing" style="left:96px;top:660px;width:89px;height:185px" role="img" aria-label="Golden circuit board texture"></div>
    <div class="part wing" style="left:590px;top:660px;width:88px;height:185px" role="img" aria-label="Golden circuit board texture"></div>
    <div class="part back" style="left:183px;top:660px;width:408px;height:182px" role="img" aria-label="Dark panel with golden sparks">
      <div class="side-strip" style="left:0;width:74px"></div>
      <div class="side-strip" style="right:0;width:74px"></div>
      <div class="tab" style="left:27px;top:1px;width:20px;height:39px;clip-path:polygon(0 0,100% 0,100% 100%,0 80%)"></div>
      <div class="tab" style="left:361px;top:120px;width:20px;height:62px;clip-path:polygon(0 10%,100% 0,100% 100%,0 100%)"></div>
      <div class="maker flip" style="left:192px;top:22px">MANUFACTURER:<br>KORVEL Marta Zielna<br>ul. Lipowa 12<br>62-300 Wrzesnia, Poland<br>Made in China</div>
      <div class="web flip" style="left:97px;top:25px">www.vireocell.pl</div>
      <div class="certs flip" style="left:97px;top:41px"><i class="sq"></i><i class="sq"></i><i></i><i></i></div>
    </div>
    <div class="part band" style="left:182px;top:842px;width:410px;height:72px">
      <div class="brand flip" style="left:103px;top:24px;font-size:21px">Vireo<span class="sub">CELLWORKS</span></div>
      <div class="label flip" style="left:230px;top:23px;width:124px;height:20px"><b>AC&nbsp;</b><span>ADAPTER</span></div>
    </div>
    <div class="part front" style="left:193px;top:914px;width:387px;height:171px">
      <div class="brand" style="left:90px;top:11px;font-size:21px">Vireo<span class="sub">CELLWORKS</span></div>
      <div class="photo laptop" style="left:170px;top:42px;width:114px;height:76px" role="img" aria-label="Laptop with glowing golden screen"></div>
      <div class="laptop-base" style="left:150px;top:118px;width:154px"></div>
      <div class="headline" style="left:88px;top:125px;font-size:17px"><span class="w">AC</span><span class="g">ADAPTER</span></div>
      <div class="badge" style="left:217px;top:149px;width:82px">PREMIUM ACCESSORIES</div>
    </div>
    <div class="part bottom" style="left:194px;top:1085px;width:386px;height:82px">
      <div class="stripe" style="left:36px;top:27px;width:52px;height:19px"></div>
      <div class="features" style="left:96px;top:30px">
        <div class="feature"><svg viewBox="0 0 10 12"><path d="M5 0L10 2v4c0 3-2.5 5-5 6C2.5 11 0 9 0 6V2z" fill="#fff"/><rect x="4.4" y="2.5" width="1.2" height="5" fill="#000"/><circle cx="5" cy="8" r="1.3" fill="#000"/></svg><p>Overheat<small>Protection</small></p></div>
        <div class="feature"><svg viewBox="0 0 10 12"><path d="M5 0L10 2v4c0 3-2.5 5-5 6C2.5 11 0 9 0 6V2z" fill="#fff"/><path d="M5.5 2L3.5 6.5h2L4.5 10l2.5-5h-2z" fill="#000"/></svg><p>Overvoltage<small>Protection</small></p></div>
        <div class="feature"><svg viewBox="0 0 10 12"><path d="M5 0L10 2v4c0 3-2.5 5-5 6C2.5 11 0 9 0 6V2z" fill="#fff"/><rect x="2" y="5.5" width="6" height="1" fill="#000"/><rect x="4.5" y="3" width="1" height="6" fill="#000"/></svg><p>Overcurrent<small>Protection</small></p></div>
        <div class="feature"><svg viewBox="0 0 10 12"><path d="M5 0L10 2v4c0 3-2.5 5-5 6C2.5 11 0 9 0 6V2z" fill="#fff"/><path d="M5 3l3 5H2z" fill="#000"/></svg><p>Short-circuit<small>Protection</small></p></div>
      </div>
    </div>
  </section>

</div>
</body>
</html>
```